Building Maintenance Flyer specialising in hot and silent pressure cleaning

Hi. I love this flyer. I would like something similar but with hot water pressure washing and building maintenance

Ferro Lane & Services provides high pressure steam cleaning and water blasting services throughout Brisbane and surrounding areas, covering the Industrial, Commercial, Strata and Residential property owners sectors.

FLS combining the cleaning power of heat with state-of-the-art silent equipment, accredited technicians and a steadfast commitment to the environment. We offer the best Prompt, Professional Service.

Fully Accredited & Certified Technicians
100% Satisfaction Guaranteed
We are a family owned and operated business and love what we do. No job is too big or too small and we take pride in our work.
All of our services are undertaken using industry leading equipment and, providing safe and superior results.

Our business is covered by 20 million full public liability insurance and we operate within strict health & safety guidelines, providing all our clients with complete peace of mind. Project plans and risk assessments can also be provided upon request.

BODY CORPORATES

BUILDING FAÇADE CLEANING

CAR PARKS – underground, single and multi level

DRIVE THRU

FOOD PRODUCTION FACILITIES CLEANING SANITISING

SHOPPING CENTRES

BIRD MANAGEMENT AND DECONTAMINATION

GENERAL MAINTENANCE

CONSTRUCTION CLEAN UPS

SPILL MANAGEMENT

CONCRETE CLEANING AND DEGRASING

CONCRETE SEALING

FACTORY CLEANING & CLEAN UP

ENVIRONMENTAL DECONTAMINATION OF HEAVY VEHICLES AND EQUIPMENT

SITE CLEANS AND RUBBISH REMOVAL

MANUFACTURING PLANTS

Target Market(s)

Facility Managers, Commercial and Industrial Property Owners, Property Managers, Schools, Restaurants,

Industry/Entity Type

Pressure Cleaning

Font styles to use
Sans Serif

Colors
0293ce
00a990
33a6d7
33b8a4

Requirements
Must have
• SILENT HOT WATER PRESSURE CLEANING
Runs up to 120 Degrees Celsius
SANITISING - Bin areas, outdoor areas, cafe's, restaurants, schools, drive thru's
Blue's and Greens to link in with our logo

```html
<!DOCTYPE html>
<html lang="en">
<head>
<meta charset="utf-8">
<title>Ferro Lane &amp; Services – Silent Hot Water Pressure Cleaning</title>
<link rel="stylesheet" href="https://fonts.googleapis.com/css2?family=Jost:wght@400;500;600;700;800&family=Barlow+Condensed:wght@500;600;700&display=swap">
<style>
  :root {
    --brand-blue: #2362b0;
    --brand-teal: #09b5aa;
    --sky: #8fcbea;
    --ink: #111111;
    --grey: #808080;
    --paper: #ffffff;
    --ice: #d3ebfa;
  }
  html, body {
    margin: 0;
    width: 1200px;
    height: 1200px;
    overflow: hidden;
    background: var(--paper);
    font-family: "Jost", sans-serif;
  }
  .flyer {
    position: absolute;
    left: 71px;
    top: 227px;
    width: 1702px;
    height: 1202px;
    transform: scale(0.6211);
    transform-origin: 0 0;
    overflow: hidden;
    background: var(--paper);
    box-shadow: 0 2px 10px rgba(0,0,0,.25);
  }
  .flyer-shapes { position: absolute; inset: 0; }
  .brand {
    position: absolute;
    left: 1330px;
    top: 105px;
    display: flex;
    align-items: center;
    gap: 18px;
  }
  .brand-dot { width: 34px; height: 34px; border-radius: 50%; background: var(--brand-teal); }
  .brand-name {
    font: 700 92px/1 "Jost", sans-serif;
    color: var(--brand-blue);
    letter-spacing: 2px;
  }
  .headline {
    position: absolute;
    right: 66px;
    top: 290px;
    margin: 0;
    text-align: right;
    font: 700 128px/1 "Jost", sans-serif;
    color: var(--brand-blue);
    letter-spacing: 1px;
  }
  .subhead {
    position: absolute;
    right: 66px;
    top: 405px;
    margin: 0;
    font: 600 76px/1 "Barlow Condensed", sans-serif;
    color: var(--grey);
    letter-spacing: -0.5px;
  }
  .intro, .detail {
    position: absolute;
    left: 825px;
    width: 830px;
    margin: 0;
    color: var(--ink);
  }
  .intro { top: 500px; font: 700 27.5px/31px "Jost", sans-serif; }
  .detail { top: 643px; font: 400 26.5px/31px "Jost", sans-serif; }
  .solutions {
    position: absolute;
    left: 65px;
    top: 700px;
    color: var(--paper);
  }
  .solutions-title { margin: 0 0 14px; font: 600 60px/1.15 "Jost", sans-serif; letter-spacing: -0.5px; }
  .solutions-list { list-style: none; margin: 0; padding: 0; }
  .solutions-list li {
    display: flex;
    align-items: center;
    gap: 12px;
    font: 400 36px/44px "Jost", sans-serif;
  }
  .tick { width: 30px; height: 30px; flex: none; }
  .contact {
    position: absolute;
    left: 820px;
    top: 968px;
  }
  .contact-row { display: flex; align-items: center; }
  .contact-phone { font: 600 62px/70px "Jost", sans-serif; color: var(--brand-blue); }
  .contact-line { font: 700 38px/52px "Jost", sans-serif; color: var(--brand-blue); }
  .contact-icon { flex: none; }
  .contact-divider {
    position: absolute;
    left: 1348px;
    top: 975px;
    width: 2px;
    height: 168px;
    background: #bbbbbb;
  }
  .sanitising {
    position: absolute;
    left: 1402px;
    top: 970px;
    margin: 0;
    font: 600 29px/34px "Jost", sans-serif;
    color: var(--ink);
  }
  .temp-label {
    position: absolute;
    left: 615px;
    top: 812px;
    width: 156px;
    text-align: center;
    color: var(--brand-blue);
  }
  .temp-label small { display: block; font: 400 17px/1 "Jost", sans-serif; letter-spacing: .5px; }
  .temp-label strong { display: block; font: 700 60px/1 "Barlow Condensed", sans-serif; margin-top: 4px; }
</style>
</head>
<body>
<div class="flyer">
  <svg class="flyer-shapes" viewBox="0 0 1702 1202" width="1702" height="1202">
    <defs>
      <linearGradient id="photoTone" x1="0" y1="0" x2="1" y2="1">
        <stop offset="0" stop-color="#4b5560"/>
        <stop offset=".45" stop-color="#6e7b87"/>
        <stop offset=".75" stop-color="#7f8f6a"/>
        <stop offset="1" stop-color="#a8b0b4"/>
      </linearGradient>
      <linearGradient id="lowerPanel" x1="0" y1="0" x2="1" y2="0">
        <stop offset=".35" stop-color="#ffffff"/>
        <stop offset="1" stop-color="#d3ebfa"/>
      </linearGradient>
      <linearGradient id="panelShade" x1="0" y1="0" x2="0" y2="1">
        <stop offset="0" stop-color="#9a9a9a"/>
        <stop offset="1" stop-color="#ffffff" stop-opacity="0"/>
      </linearGradient>
    </defs>

    <rect class="photo" role="img" aria-label="Photo: technician in overalls pressure washing a paved path beside a dark brick wall" x="0" y="0" width="1702" height="1202" fill="url(#photoTone)"/>

    <ellipse cx="330" cy="760" rx="420" ry="190" fill="#ffffff" opacity=".22"/>

    <path class="swoosh-teal" d="M1000 0 C820 110 700 380 590 640 L640 660 C760 400 890 120 1090 0 Z" fill="var(--brand-teal)"/>
    <path class="swoosh-black" d="M1060 0 C860 130 760 400 650 625 C735 700 790 800 812 885 L860 885 C840 780 780 690 700 620 C810 360 920 120 1100 0 Z" fill="#000"/>

    <path class="panel-shade" d="M1702 690 C1420 840 1080 870 840 880 L840 920 C1100 910 1450 870 1702 760 Z" fill="url(#panelShade)"/>
    <path class="text-panel" d="M1085 0 L1702 0 L1702 700 C1420 835 1080 868 815 875 C790 790 740 690 675 622 C790 360 900 120 1085 0 Z" fill="var(--paper)"/>

    <path class="lower-panel" d="M720 1202 C758 1080 768 980 770 905 C1100 895 1450 852 1702 800 L1702 1202 Z" fill="url(#lowerPanel)"/>
    <path class="band-teal" d="M770 882 C1100 875 1450 830 1702 768 L1702 818 C1450 872 1100 908 770 918 Z" fill="var(--brand-teal)"/>

    <path class="solutions-panel" d="M0 725 C140 610 440 585 625 680 C740 745 790 860 778 990 C768 1090 742 1160 722 1202 L0 1202 Z" fill="var(--brand-blue)"/>
    <path d="M690 740 C760 830 770 960 745 1070 C735 1120 715 1170 700 1202 L618 1202 C650 1140 672 1080 680 1010 C692 900 680 810 640 740 Z" fill="var(--sky)"/>
    <path d="M720 780 C770 870 778 980 760 1080 C750 1130 735 1175 722 1202 L665 1202 C690 1150 705 1100 712 1040 C724 940 715 850 680 780 Z" fill="#1f6fbf" opacity=".9"/>

    <g class="guarantee-badge">
      <circle cx="572" cy="700" r="94" fill="#fff" stroke="#fff" stroke-width="6" stroke-dasharray="6 5"/>
      <circle cx="572" cy="700" r="84" fill="#fff" stroke="var(--brand-blue)" stroke-width="4"/>
      <circle cx="572" cy="700" r="50" fill="var(--brand-blue)"/>
      <path id="badgeTop" d="M506 700 A66 66 0 0 1 638 700" fill="none"/>
      <path id="badgeBottom" d="M510 706 A62 62 0 0 0 634 706" fill="none"/>
      <text font-family="Jost, sans-serif" font-weight="700" font-size="13" fill="var(--brand-blue)" letter-spacing="1.5">
        <textPath href="#badgeTop" startOffset="50%" text-anchor="middle">SATISFACTION GUARANTEE</textPath>
      </text>
      <text font-family="Jost, sans-serif" font-weight="700" font-size="13" fill="var(--brand-blue)" letter-spacing="1.5">
        <textPath href="#badgeBottom" startOffset="50%" text-anchor="middle">SATISFACTION GUARANTEE</textPath>
      </text>
      <text x="572" y="712" text-anchor="middle" font-family="Barlow Condensed, sans-serif" font-weight="700" font-size="40" fill="#fff">100%</text>
      <text x="516" y="704" text-anchor="middle" font-size="12" fill="var(--brand-blue)">★</text>
      <text x="628" y="704" text-anchor="middle" font-size="12" fill="var(--brand-blue)">★</text>
    </g>

    <circle class="temp-dial" cx="693" cy="845" r="80" fill="#fff"/>
    <circle cx="736" cy="786" r="29" fill="var(--brand-blue)"/>
    <path d="M736 770 C742 778 748 784 746 793 C744 800 738 803 736 803 C730 803 725 798 726 791 C727 786 731 784 731 778 C734 781 735 784 736 787 C738 782 738 776 736 770 Z" fill="none" stroke="#fff" stroke-width="2"/>
  </svg>

  <div class="brand">
    <span class="brand-dot"></span>
    <span class="brand-name">FLS</span>
  </div>

  <h1 class="headline">SILENT HOT</h1>
  <h2 class="subhead">WATER PRESSURE CLEANING</h2>

  <p class="intro">Ferro Lane &amp; Services provides high pressure steam cleaning and water blasting services throughout Brisbane and surrounding areas, covering the Industrial, Commercial, Strata and Residential property owners sectors.</p>
  <p class="detail">FLS combining the cleaning power of heat with state-of-the-art silent equipment, accredited technicians and a steadfast commitment to the environment. We offer the best Prompt, Professional Service.</p>

  <div class="temp-label">
    <small>RUNS UP TO</small>
    <strong>120°C</strong>
  </div>

  <section class="solutions">
    <h3 class="solutions-title">Solutions For:</h3>
    <ul class="solutions-list">
      <li><svg class="tick" viewBox="0 0 30 30"><circle cx="15" cy="15" r="13" fill="none" stroke="var(--brand-teal)" stroke-width="2"/><path d="M9 15 L13.5 19.5 L21 11" fill="none" stroke="var(--brand-teal)" stroke-width="2.2"/></svg>COVID-19 Infection Control</li>
      <li><svg class="tick" viewBox="0 0 30 30"><circle cx="15" cy="15" r="13" fill="none" stroke="var(--brand-teal)" stroke-width="2"/><path d="M9 15 L13.5 19.5 L21 11" fill="none" stroke="var(--brand-teal)" stroke-width="2.2"/></svg>Building Management</li>
      <li><svg class="tick" viewBox="0 0 30 30"><circle cx="15" cy="15" r="13" fill="none" stroke="var(--brand-teal)" stroke-width="2"/><path d="M9 15 L13.5 19.5 L21 11" fill="none" stroke="var(--brand-teal)" stroke-width="2.2"/></svg>Bin Cleaning &amp; Sanitisation</li>
      <li><svg class="tick" viewBox="0 0 30 30"><circle cx="15" cy="15" r="13" fill="none" stroke="var(--brand-teal)" stroke-width="2"/><path d="M9 15 L13.5 19.5 L21 11" fill="none" stroke="var(--brand-teal)" stroke-width="2.2"/></svg>Garden Maintenance</li>
      <li><svg class="tick" viewBox="0 0 30 30"><circle cx="15" cy="15" r="13" fill="none" stroke="var(--brand-teal)" stroke-width="2"/><path d="M9 15 L13.5 19.5 L21 11" fill="none" stroke="var(--brand-teal)" stroke-width="2.2"/></svg>Common Area Cleaning</li>
      <li><svg class="tick" viewBox="0 0 30 30"><circle cx="15" cy="15" r="13" fill="none" stroke="var(--brand-teal)" stroke-width="2"/><path d="M9 15 L13.5 19.5 L21 11" fill="none" stroke="var(--brand-teal)" stroke-width="2.2"/></svg>Bird waste removal</li>
      <li><svg class="tick" viewBox="0 0 30 30"><circle cx="15" cy="15" r="13" fill="none" stroke="var(--brand-teal)" stroke-width="2"/><path d="M9 15 L13.5 19.5 L21 11" fill="none" stroke="var(--brand-teal)" stroke-width="2.2"/></svg>Mould &amp; Mildew removal</li>
      <li><svg class="tick" viewBox="0 0 30 30"><circle cx="15" cy="15" r="13" fill="none" stroke="var(--brand-teal)" stroke-width="2"/><path d="M9 15 L13.5 19.5 L21 11" fill="none" stroke="var(--brand-teal)" stroke-width="2.2"/></svg>Oil &amp; Grease elimination</li>
    </ul>
  </section>

  <div class="contact">
    <div class="contact-row contact-phone">
      <svg class="contact-icon" width="72" height="64" viewBox="0 0 72 64"><path d="M8 6 C4 10 3 18 10 30 C18 44 30 54 42 58 C50 60 54 56 56 52 L48 44 C44 46 40 48 36 44 C30 38 24 30 22 24 C20 20 22 18 26 16 L18 4 C14 2 10 4 8 6 Z" fill="none" stroke="#999" stroke-width="2.4"/></svg>
      <span>555-0142-7788</span>
    </div>
    <div class="contact-row contact-line">
      <svg class="contact-icon" width="72" height="40" viewBox="0 0 72 40"><rect x="20" y="10" width="32" height="22" fill="none" stroke="#999" stroke-width="2"/><path d="M20 10 L36 23 L52 10 M20 32 L31 21 M52 32 L41 21" fill="none" stroke="#999" stroke-width="2"/></svg>
      <span>hello@ferrolane.example</span>
    </div>
    <div class="contact-row contact-line">
      <svg class="contact-icon" width="72" height="40" viewBox="0 0 72 40"><circle cx="36" cy="21" r="15" fill="none" stroke="#999" stroke-width="2"/><ellipse cx="36" cy="21" rx="6" ry="15" fill="none" stroke="#999" stroke-width="2"/><path d="M21 21 H51 M24 13 H48 M24 29 H48" stroke="#999" stroke-width="2"/></svg>
      <span>www.ferrolane.example</span>
    </div>
  </div>

  <div class="contact-divider"></div>

  <p class="sanitising">Sanitising bin<br>areas, outdoor<br>areas, cafe’s,<br>restaurants, schools<br>&amp; drive thru’s</p>
</div>
</body>
</html>
```